Moder Business Card Design for Renewables Business

Need a business card design for my business. We collect & repurpose spent coffee ground from cafes. The cards will be made from recycled paper. Needs to fit our corporate colour scheme of white, green & brown (see logo for colour codes). Eco friendly, modern, intresting & eye catching.
This card needs to convey the message of the business and fit into its mantra of eco-friendly, sustainable etc.

Target Market(s)

Cafe Owners, Coffee Drinkers, Recycling Companies, Farmers

Industry/Entity Type

Recycling

Contact Information for Business Card

Name; Peter Halloran
Phone; 0412 386 527
e-mail; info@lumatrove.com.au
website; www.lumatrove.com.au

Font styles to use
Sans Serif
Script

Colors

Designer to choose colors to be used in the design.

Requirements
Must have
• FRONT;
• Logo, Name (Peter Halloran), phone number, e-mail address, website
• BACK;
• On the back in cursive text; 'GOOD GROUNDS FOR A GREENER DAY'
• Small facebook & Instagram logos with text 'Lumatrove'
Should not have
• messy design

```html
<!DOCTYPE html>
<html lang="en">
<head>
<meta charset="utf-8">
<title>Lumatrove Business Card</title>
<link rel="stylesheet" href="https://fonts.googleapis.com/css2?family=Open+Sans:wght@400;600;700&family=Dancing+Script:wght@500&display=swap">
<style>
  :root {
    --backdrop: #2a2e32;
    --paper: #f7f6f3;
    --brown: #6b3a1f;
    --green: #6aa83a;
    --muted: #7a6a5e;
    --rule: #8a5a3c;
  }
  * { margin: 0; padding: 0; box-sizing: border-box; }
  html, body { width: 1200px; height: 900px; overflow: hidden; }
  body {
    background: var(--backdrop);
    font-family: "Open Sans", Arial, sans-serif;
    position: relative;
  }
  .card {
    position: absolute;
    top: 300px;
    width: 520px;
    height: 300px;
    background: var(--paper);
    border-radius: 22px;
    color: var(--brown);
  }
  .card--front { left: 50px; }
  .card--back { left: 630px; }

  /* Front */
  .brand-block {
    position: absolute;
    left: 40px;
    top: 48px;
    width: 190px;
    text-align: center;
  }
  .brand-dot {
    width: 96px;
    height: 96px;
    border-radius: 50%;
    background: var(--brown);
    margin: 0 auto 18px;
  }
  .brand-name {
    font-weight: 700;
    font-size: 26px;
    letter-spacing: 0.5px;
    color: var(--green);
  }
  .contact-block {
    position: absolute;
    right: 40px;
    top: 70px;
    width: 250px;
    text-align: center;
  }
  .person-name {
    font-weight: 700;
    font-size: 24px;
    letter-spacing: 0.3px;
  }
  .person-name .first { color: var(--green); }
  .person-name .last { color: var(--brown); }
  .divider {
    width: 90px;
    height: 1px;
    background: var(--rule);
    margin: 18px auto 18px;
  }
  .contact-line {
    font-size: 17px;
    line-height: 1.45;
    color: var(--brown);
  }

  /* Back */
  .tagline {
    position: absolute;
    left: 0;
    right: 0;
    top: 58px;
    text-align: center;
    font-family: "Dancing Script", cursive;
    font-size: 34px;
    color: var(--brown);
  }
  .tagline-rule {
    position: absolute;
    left: 90px;
    right: 90px;
    top: 118px;
    height: 1px;
    background: var(--rule);
  }
  .mark-dot {
    position: absolute;
    left: 50%;
    top: 140px;
    width: 40px;
    height: 40px;
    margin-left: -20px;
    border-radius: 50%;
    background: var(--brown);
  }
  .social-row {
    position: absolute;
    left: 0;
    right: 0;
    top: 196px;
    display: flex;
    justify-content: center;
    gap: 10px;
  }
  .social-dot {
    width: 20px;
    height: 20px;
    border-radius: 50%;
    background: var(--green);
  }
  .back-brand {
    position: absolute;
    left: 0;
    right: 0;
    top: 228px;
    text-align: center;
    font-size: 13px;
    letter-spacing: 4px;
    color: var(--muted);
  }
</style>
</head>
<body>
  <section class="card card--front" aria-label="Business card front">
    <div class="brand-block">
      <div class="brand-dot"></div>
      <div class="brand-name">LUMATROVE</div>
    </div>
    <div class="contact-block">
      <div class="person-name"><span class="first">PETER</span> <span class="last">HALLORAN</span></div>
      <div class="divider"></div>
      <div class="contact-line">0412 386 527</div>
      <div class="contact-line">info@lumatrove.com.au</div>
      <div class="contact-line">www.lumatrove.com.au</div>
    </div>
  </section>

  <section class="card card--back" aria-label="Business card back">
    <div class="tagline">Good Grounds For A Greener Day</div>
    <div class="tagline-rule"></div>
    <div class="mark-dot"></div>
    <div class="social-row">
      <span class="social-dot"></span>
      <span class="social-dot"></span>
    </div>
    <div class="back-brand">LUMATROVE</div>
  </section>
</body>
</html>
```